Лого и фирменный стиль для Ясные бумаги
Название, обыгрываемое в логотипе
Ясные бумаги
Какие элементы вам нужны?
Визитка, Логотип, Официальный бланк, Шаблон презентации
Подробное описание компании, продукта и целевой аудитории
Государственные корпорации, государство, банки

```html
<!DOCTYPE html>
<html lang="ru">
<head>
<meta charset="utf-8">
<title>Ясные бумаги — фирменный стиль</title>
<link href="https://fonts.googleapis.com/css2?family=Open+Sans:wght@400;700&display=swap" rel="stylesheet">
<style>
:root{
  --stage:#444444;
  --brand-red:#e31e24;
  --brand-red-light:#ee5a5e;
  --pale-red:#f9dcdd;
  --paper:#ffffff;
  --ink:#222222;
  --grey:#6e6e6e;
}
*{margin:0;padding:0;box-sizing:border-box}
html,body{width:1200px;height:900px;overflow:hidden;background:var(--stage);font-family:"Open Sans",sans-serif}
.stage{position:relative;width:1200px;height:900px}
.sheet{position:absolute;box-shadow:4px 6px 12px rgba(0,0,0,.35)}
.letterhead{left:106px;top:36px;width:577px;height:816px;background:var(--paper)}
.contacts{position:absolute;list-style:none;color:var(--ink)}
.contacts li{display:flex;align-items:center;gap:9px;height:19px;font-size:10.5px}
.contacts svg{width:14px;height:14px;flex:none}
.letterhead .contacts{left:54px;top:29px}
.wordmark{position:absolute;display:flex;align-items:center;gap:9px;font-weight:700;text-transform:uppercase;text-align:right;line-height:1.05}
.wordmark .dot{display:block}
.letterhead .wordmark{right:55px;top:33px;color:var(--grey);font-size:19px}
.letterhead .wordmark .dot{width:38px;height:38px;background:var(--brand-red)}
.rule{position:absolute;left:0;top:0}
.footer-pattern{position:absolute;left:0;top:760px;width:550px;height:32px;background:linear-gradient(90deg,var(--paper),var(--pale-red))}
.card{width:247px;height:136px}
.card-front{left:847px;top:48px;background:var(--brand-red)}
.card-front .wordmark{right:48px;top:48px;color:#fff;font-size:15px}
.card-front .wordmark .dot{width:32px;height:32px;background:#fff}
.card-back{left:847px;top:209px;background:var(--paper)}
.card-back .square{position:absolute;left:23px;top:17px;width:32px;height:32px;background:var(--brand-red)}
.person{position:absolute;right:23px;top:18px;text-align:right;color:var(--ink)}
.person .name{font-weight:700;font-size:14px;line-height:1.15;text-transform:uppercase}
.person .role{font-size:9px;margin-top:2px}
.card-back .contacts{left:23px;top:81px}
.card-back .contacts li{height:15px;font-size:8.5px;gap:8px}
.card-back .contacts svg{width:11px;height:11px}
.cover{left:514px;top:371px;width:577px;height:408px;background:var(--brand-red)}
.cover-pattern{position:absolute;left:0;top:150px;width:250px;height:106px;background:linear-gradient(90deg,var(--brand-red),var(--brand-red-light))}
.cover .wordmark{right:49px;top:175px;color:#fff;font-size:26px;gap:14px}
.cover .wordmark .dot{width:54px;height:54px;background:#fff}
</style>
</head>
<body>
<main class="stage">

  <section class="sheet letterhead">
    <ul class="contacts">
      <li><svg viewBox="0 0 14 14"><rect width="14" height="14" fill="#e31e24"/><path d="M3 7 7 3.5 11 7V11H8.2V8.5H5.8V11H3Z" fill="#fff"/></svg>Город, улица, номер офиса</li>
      <li><svg viewBox="0 0 14 14"><rect width="14" height="14" fill="#e31e24"/><rect x="3" y="4" width="8" height="6" fill="#fff"/><path d="M3 4 7 7.5 11 4" stroke="#e31e24" fill="none"/></svg>e-mail</li>
      <li><svg viewBox="0 0 14 14"><rect width="14" height="14" fill="#e31e24"/><path d="M4 3.5 5.8 3.5 6.5 5.5 5.5 6.3Q6.5 8.2 8 8.8L8.8 7.8 10.6 8.6 10.6 10.4Q6.5 10.6 4 6.5Z" fill="#fff"/></svg>+7 (000) 000-00-00</li>
    </ul>
    <div class="wordmark"><span>Ясные<br>бумаги</span><span class="dot"></span></div>
    <svg class="rule" width="577" height="120" viewBox="0 0 577 120">
      <line x1="0" y1="112" x2="548" y2="112" stroke="#e31e24" stroke-width="1.2"/>
      <circle cx="548" cy="112" r="2.5" fill="#e31e24"/>
    </svg>
    <div class="footer-pattern" role="img" aria-label="Декоративный узор из линий в красных тонах"></div>
  </section>

  <section class="sheet card card-front">
    <div class="wordmark"><span>Ясные<br>бумаги</span><span class="dot"></span></div>
  </section>

  <section class="sheet card card-back">
    <span class="square"></span>
    <div class="person">
      <p class="name">Имя Отчество<br>Фамилия</p>
      <p class="role">должность</p>
    </div>
    <svg class="rule" width="247" height="136" viewBox="0 0 247 136">
      <line x1="0" y1="77" x2="221" y2="77" stroke="#e31e24" stroke-width="1"/>
      <circle cx="221" cy="77" r="2" fill="#e31e24"/>
    </svg>
    <ul class="contacts">
      <li><svg viewBox="0 0 14 14"><rect width="14" height="14" fill="#e31e24"/><path d="M3 7 7 3.5 11 7V11H8.2V8.5H5.8V11H3Z" fill="#fff"/></svg>Город, улица, номер офиса</li>
      <li><svg viewBox="0 0 14 14"><rect width="14" height="14" fill="#e31e24"/><rect x="3" y="4" width="8" height="6" fill="#fff"/><path d="M3 4 7 7.5 11 4" stroke="#e31e24" fill="none"/></svg>e-mail</li>
      <li><svg viewBox="0 0 14 14"><rect width="14" height="14" fill="#e31e24"/><path d="M4 3.5 5.8 3.5 6.5 5.5 5.5 6.3Q6.5 8.2 8 8.8L8.8 7.8 10.6 8.6 10.6 10.4Q6.5 10.6 4 6.5Z" fill="#fff"/></svg>+7 (000) 000-00-00</li>
    </ul>
  </section>

  <section class="sheet cover">
    <div class="cover-pattern" role="img" aria-label="Декоративный узор из светлых линий на красном фоне"></div>
    <div class="wordmark"><span>Ясные<br>бумаги</span><span class="dot"></span></div>
  </section>

</main>
</body>
</html>
```